依頼概要
今回デザインを依頼したいのは、オーガニックハーブティー3種(東ティモールのマウベシ郡産)のパッケージラベルです。
豊かな自然溢れる山々に囲まれた標高約1500メートルに位置するマウベシ郡。きれいな水と空気が育んだ自生のハーブを地元の女性グループが採取し、太陽の恵みをたっぷり受けて自然乾燥させます。加工プロセスのすべてを手作業で丁寧に行うことで出来るのがこの香り高いオーガニックのハーブティーです。すべての過程において、農薬や化学肥料は一切使われていません。
これらのハーブは東ティモールで古くから伝統薬として利用されてきたもので、彼らの知恵がつまったものです。下記サイトに生産者や生産現場の情報がありますので、雰囲気を感じていただけるかと思います。
https://www.hanuvel.org/report/timor-leste/timor_womanqol/6920/

※今後、このシリーズでハーブティーの種類が増える可能性もあります。
※デザイン決定後にラベルと同じイメージで簡単なリーフレットを作成していただきます

【ラベルの大きさ】
H95mm × W160mm (縦・横)
(使用するパッケージは、光沢のある白いチャック付きスタンド袋。袋の表面を覆うくらいの比較的大きなラベルです。)
【パッケージの大きさ】
H160mm × W190mm マチは約80mmです

【ラベルのイメージ】
・全体(背景)の色:ティーごとに異なるものを使用。下記の各ティーの詳細にあるイメージカラーをそれぞれ使う。
無地ではなく、自模様のデザインが入ったものが希望。
色味はビビッドよりもやわらかい感じで。
・自模様のデザイン:色と同様、ハーブティーごとに模様を変えたい。

・記載したい文字:
① 商品名→ 例:オーガニックハーブティー No.1
② 各ティーの種類名→ 例:月桃&ライムリーフ ブレンド
③ 効能を一言で表現したもの→ 例:Beauty
④ 「有機栽培」と有機KMRマーク(後日添付します)
⑤ 弊社のロゴ
⑥ 「東ティモール産」

【各商品の情報】※詳細は別途追記に記載します
A ①オーガニックハーブティーNo.1②月桃&ライムリーフブレンド③Beauty
イメージカラー (青よりの)薄紫

B ①オーガニックハーブティーNo.2②ツボクサ&ミントブレンド③Refresh
イメージカラー 緑

C ①オーガニックハーブティーNo.3②レモングラス&アボガドリーフブレンド③Health
イメージカラー 黃

何かご不明な点がありましたらお気軽にご質問ください。
どうぞよろしくお願いいたします。

イメージのご参考に各商品の説明です

A 月桃&ライムリーフブレンド
少しスパイシーな香りの月桃と香り高いライムリーフのブレンド。
非常に多くのポリフェノールを含む月桃は、体の酸化を防いで若さを保つと言われ、とても注目されているハーブです。体を中から温める効果もあり、血管の若さを保つと言われるライムリーフとの組み合わせで、内側から肌と体を整えてくれます。
ほのかに甘く、深みがあり、後味もさっぱりしています。お子さまから高齢者まで、安心してお飲みいただけます。

B ツボクサ&ミントブレンド
くせのない爽やかな草原の香りがするツボクサに、穏やかな清涼感のミントがブレンドされたとても飲みやすいハーブティーです。
東ティモールで「知性のハーブ」と呼ばれるツボクサは、脳や血管の老化を防ぐ他、心を鎮める効果があると言われています。
ミントは胃もたれや消化不良を改善する効果があるとされ、ストレスがお腹にくる方にもおすすめです。

C レモングラス&アボガドリーフブレンド
レモンに似た香りのレモングラスとくせのないアボガドリーフのブレンド。酸味はありません。
レモングラスには殺菌作用がある成分が含まれ、風邪予防に使われる他、このさわやかな香りには集中力を高める効果もあると言われています。
利尿作用もあり、むくみ対策にも。ビタミンEを多く含むアボガドリーフは体を温め、疲労回復効果があり、東ティモールでは古くから胃腸を整えるハーブとしても使われています。
日々の体調管理にぴったりのさまざまな効果を持つブレンドです。
有機KMRマークを添付します。
弊社ロゴの添付を追加しました。
また、一部金額を上方修正しました。

引き続き、みなさまよろしくお願いいたします。
何度も失礼します。
有機KMRマークがうまく添付されていなかったので追加します。
みなさま提案いただきありがとうございます。
選考に難航しておりますので、多くの目で選考して行くために締め切りを5日間延長させていただきます。
また、選定確約も設定いたしました。

字体の部分でもう少し、オリジナリティ、オシャレ感が欲しいなと思っています。
今後個別の連絡もさせていただくかと思いますので、引き続きよろしくお願いいたします。

生産地とハーブティーの雰囲気が、弊社の希望に1番近いイメージでデザインされていました。

たくさんの提案をいただきありがとうございました。
様々なデザインを見ることが出来てこちらも勉強になりました。

またコンペをする際にはよろしくお願いいたします。

```html
<!DOCTYPE html>
<html lang="ja">
<head>
<meta charset="utf-8">
<title>オーガニックハーブティー ラベル</title>
<link rel="stylesheet" href="https://fonts.googleapis.com/css2?family=Noto+Serif+JP:wght@500;700;900&family=Playfair+Display:ital,wght@0,500;1,500&display=swap">
<style>
  :root {
    --page: #ffffff;
    --ink: #3a3530;
    --rule: #8d857c;
    --frame: #c9bfae;
    --panel: #ffffff;
    --beauty-bg: #cfd0ec;
    --beauty-band: #c0c2e4;
    --beauty-line: #e4e2f3;
    --refresh-bg: #cdeadf;
    --refresh-band: #bde0d2;
    --refresh-line: #e2f3ec;
    --health-bg: #f5f3c8;
    --health-band: #ece8b2;
    --health-line: #f9f8e0;
    --seal: #5fa25a;
    --cert: #2f2f2f;
    --icon: #d8d2c6;
  }
  * { margin: 0; padding: 0; box-sizing: border-box; }
  html, body { width: 1200px; height: 2400px; overflow: hidden; background: var(--page); }
  body { position: relative; font-family: "Noto Serif JP", serif; color: var(--ink); }

  .label {
    position: absolute; left: 32px; width: 1136px; height: 720px;
    overflow: hidden;
  }
  .label--beauty  { top: 40px; }
  .label--refresh { top: 840px; }
  .label--health  { top: 1640px; }

  .label__pattern { position: absolute; inset: 0; }
  .label--beauty .label__pattern {
    background:
      repeating-linear-gradient(90deg,
        transparent 0 70px, var(--beauty-line) 70px 74px,
        transparent 74px 108px, var(--beauty-band) 108px 138px,
        transparent 138px 176px),
      var(--beauty-bg);
  }
  .label--refresh .label__pattern {
    background:
      repeating-linear-gradient(90deg,
        transparent 0 70px, var(--refresh-line) 70px 74px,
        transparent 74px 108px, var(--refresh-band) 108px 138px,
        transparent 138px 176px),
      var(--refresh-bg);
  }
  .label--health .label__pattern {
    background:
      repeating-linear-gradient(90deg,
        transparent 0 70px, var(--health-line) 70px 74px,
        transparent 74px 108px, var(--health-band) 108px 138px,
        transparent 138px 176px),
      var(--health-bg);
  }

  .panel {
    position: absolute; left: 308px; top: 100px; width: 520px; height: 520px;
    background: var(--panel);
    display: flex; flex-direction: column; align-items: center;
    padding: 28px;
  }
  .panel > * { flex-shrink: 0; }
  .panel__frame {
    position: absolute; inset: 14px; border: 2px solid var(--frame);
  }
  .panel__icon {
    margin-top: 30px; width: 52px; height: 40px; border-radius: 20px;
    background: var(--icon);
  }
  .panel__benefit {
    font-family: "Playfair Display", serif; font-style: italic; font-weight: 500;
    font-size: 58px; line-height: 1; margin-top: 24px; letter-spacing: 1px;
    white-space: nowrap;
  }
  .panel__rule { width: 400px; height: 2px; background: var(--rule); }
  .panel__rule--top { margin-top: 24px; }
  .panel__blend {
    font-weight: 700; font-size: 22px; line-height: 1.4; letter-spacing: 1px;
    padding: 14px 0; white-space: nowrap;
  }
  .panel__product {
    font-weight: 900; font-size: 34px; line-height: 1.4; letter-spacing: 1px;
    margin-top: 18px; white-space: nowrap;
  }
  .panel__seal {
    margin-top: 24px; width: 76px; height: 76px; border-radius: 50%;
    background: var(--seal);
  }

  .cert {
    position: absolute; right: 26px; bottom: 26px;
    display: flex; flex-direction: column; align-items: center;
  }
  .cert__mark { width: 84px; height: 84px; border-radius: 50%; border: 4px solid var(--cert); }
  .cert__body { font-size: 20px; font-weight: 500; margin-top: 8px; color: var(--cert); white-space: nowrap; }
  .cert__code { font-size: 14px; color: var(--cert); }
</style>
</head>
<body>

<section class="label label--beauty">
  <div class="label__pattern" role="img" aria-label="淡い青紫の地に縦に並ぶ雪の結晶とジグザグの地模様"></div>
  <div class="panel">
    <div class="panel__frame"></div>
    <div class="panel__icon" role="img" aria-label="草花の小さな飾り"></div>
    <div class="panel__benefit">Beauty</div>
    <div class="panel__rule panel__rule--top"></div>
    <div class="panel__blend">月桃＆ライムリーフブレンド</div>
    <div class="panel__rule"></div>
    <div class="panel__product">オーガニックハーブティー</div>
    <div class="panel__seal" role="img" aria-label="有機栽培の丸いマーク"></div>
  </div>
  <div class="cert">
    <div class="cert__mark" role="img" aria-label="有機KMRマーク"></div>
    <div class="cert__body">ベルタ認証機構</div>
    <div class="cert__code">CERT-0158</div>
  </div>
</section>

<section class="label label--refresh">
  <div class="label__pattern" role="img" aria-label="淡い緑の地に縦に並ぶ雪の結晶とジグザグの地模様"></div>
  <div class="panel">
    <div class="panel__frame"></div>
    <div class="panel__icon" role="img" aria-label="湯気の立つティーカップの小さな飾り"></div>
    <div class="panel__benefit">Refresh</div>
    <div class="panel__rule panel__rule--top"></div>
    <div class="panel__blend">ツボクサ＆ミントブレンド</div>
    <div class="panel__rule"></div>
    <div class="panel__product">オーガニックハーブティー</div>
    <div class="panel__seal" role="img" aria-label="有機栽培の丸いマーク"></div>
  </div>
  <div class="cert">
    <div class="cert__mark" role="img" aria-label="有機KMRマーク"></div>
    <div class="cert__body">ベルタ認証機構</div>
    <div class="cert__code">CERT-0158</div>
  </div>
</section>

<section class="label label--health">
  <div class="label__pattern" role="img" aria-label="淡い黄色の地に縦に並ぶ雪の結晶とジグザグの地模様"></div>
  <div class="panel">
    <div class="panel__frame"></div>
    <div class="panel__icon" role="img" aria-label="麦の穂の小さな飾り"></div>
    <div class="panel__benefit">Health</div>
    <div class="panel__rule panel__rule--top"></div>
    <div class="panel__blend">レモングラス＆アボガドリーフブレンド</div>
    <div class="panel__rule"></div>
    <div class="panel__product">オーガニックハーブティー</div>
    <div class="panel__seal" role="img" aria-label="有機栽培の丸いマーク"></div>
  </div>
  <div class="cert">
    <div class="cert__mark" role="img" aria-label="有機KMRマーク"></div>
    <div class="cert__body">ベルタ認証機構</div>
    <div class="cert__code">CERT-0158</div>
  </div>
</section>

</body>
</html>
```